PowerPoint Template for Regional Harmony Institute. Website is www.regionalharmonyinstitute.com

The tagline for the Center is "Connecting the brightest minds in healthcare"

```html
<!DOCTYPE html>
<html lang="en">
<head>
<meta charset="utf-8">
<title>Regional Harmony Institute — Presentation Template</title>
<link rel="stylesheet" href="https://fonts.googleapis.com/css2?family=Montserrat:wght@300;400;600;700&family=Open+Sans:wght@400;600&display=swap">
<style>
  :root{
    --navy:#1b3a6b;
    --navy-soft:#2e5590;
    --ink:#2b2f36;
    --grey:#8d929b;
    --rule:#c9ced8;
    --paper:#ffffff;
    --page:#ffffff;
    --photo-a:#d8e2ee;
    --photo-b:#8fa6c4;
  }
  html,body{margin:0;padding:0;overflow:hidden;background:var(--page);}
  .canvas{position:relative;width:801px;height:1200px;overflow:hidden;background:var(--page);}
  .slide{position:absolute;width:238px;height:135px;background:var(--paper);
    box-shadow:0 1px 3px rgba(0,0,0,.28);}
  .slide svg{display:block;width:100%;height:100%;}
  .col-l{left:150px}.col-r{left:405px}
  .title{font:700 6.5px 'Montserrat',sans-serif;fill:var(--navy);letter-spacing:.2px}
  .head{font:700 5px 'Montserrat',sans-serif;fill:var(--navy)}
  .lead{font:600 3.2px 'Open Sans',sans-serif;fill:var(--navy)}
  .body{font:400 2.6px 'Open Sans',sans-serif;fill:var(--grey)}
  .label{font:400 3.2px 'Open Sans',sans-serif;fill:var(--navy)}
  .foot{font:600 2.2px 'Montserrat',sans-serif;fill:var(--navy)}
  .brand{font:600 7px 'Montserrat',sans-serif;fill:var(--navy)}
  .ring{fill:none;stroke:var(--navy);stroke-width:5}
  .node{fill:#fff;stroke:var(--navy);stroke-width:1.2}
  .line{stroke:var(--rule);stroke-width:.6;fill:none}
  .navyfill{fill:var(--navy)}
</style>
</head>
<body>
<div class="canvas">
<svg width="0" height="0" style="position:absolute">
  <defs>
    <linearGradient id="photo" x1="0" y1="0" x2="1" y2="1">
      <stop offset="0" stop-color="#e6edf5"/><stop offset="1" stop-color="#9fb3cc"/>
    </linearGradient>
    <linearGradient id="photoDark" x1="0" y1="0" x2="1" y2="0">
      <stop offset="0" stop-color="#6d86a8"/><stop offset="1" stop-color="#a9bbd2"/>
    </linearGradient>
  </defs>
</svg>

<!-- Row 1 -->
<div class="slide col-l" style="top:20px">
<svg viewBox="0 0 300 170">
  <circle role="img" aria-label="Photo of two clasped hands" cx="78" cy="85" r="62" fill="url(#photo)"/>
  <circle class="ring" cx="78" cy="85" r="68" pathLength="100" stroke-dasharray="40 60" transform="rotate(95 78 85)"/>
  <text class="head" x="284" y="42" text-anchor="end">CONNECTING THE BRIGHTEST</text>
  <text class="head" x="284" y="49" text-anchor="end">MINDS IN HEALTHCARE</text>
  <text class="body" x="284" y="56" text-anchor="end">LOREM IPSUM DOLOR | 01.01.2018</text>
  <circle class="node" cx="208" cy="142" r="6"/>
  <text class="brand" x="218" y="141">REGIONAL HARMONY</text>
  <text class="brand" x="218" y="148" style="font-size:5px">INSTITUTE</text>
</svg>
</div>
<div class="slide col-r" style="top:20px">
<svg viewBox="0 0 300 170">
  <text class="title" x="16" y="20">LOREM IPSUM</text>
  <circle class="node" cx="281" cy="18" r="6"/>
  <line class="line" x1="103" y1="40" x2="103" y2="168"/>
  <g class="label">
    <circle class="navyfill" cx="103" cy="50" r="1.3"/><text x="110" y="51">Lorem Ipsum Dolor Sit Amet</text>
    <circle class="navyfill" cx="103" cy="68" r="1.3"/><text x="110" y="69">Lorem Ipsum Dolor Sit Amet</text>
    <circle class="navyfill" cx="103" cy="86" r="1.3"/><text x="110" y="87">Lorem Ipsum Dolor Sit Amet</text>
    <circle class="navyfill" cx="103" cy="104" r="1.3"/><text x="110" y="105">Lorem Ipsum Dolor Sit Amet</text>
    <circle class="navyfill" cx="103" cy="122" r="1.3"/><text x="110" y="123">Lorem Ipsum Dolor Sit Amet</text>
    <circle class="navyfill" cx="103" cy="140" r="1.3"/><text x="110" y="141">Lorem Ipsum Dolor Sit Amet</text>
  </g>
  <circle class="line" cx="20" cy="162" r="3"/>
  <text class="foot" x="284" y="163" text-anchor="end">REGIONAL HARMONY INSTITUTE</text>
</svg>
</div>

<!-- Row 2 -->
<div class="slide col-l" style="top:166px">
<svg viewBox="0 0 300 170">
  <rect role="img" aria-label="Blue-toned photo of a doctor with a stethoscope" width="300" height="170" fill="url(#photoDark)"/>
  <text x="145" y="58" text-anchor="end" style="font:300 12px 'Montserrat',sans-serif;fill:#fff">Lorem Ipsum</text>
  <text x="145" y="74" text-anchor="end" style="font:300 12px 'Montserrat',sans-serif;fill:#fff">Dolor Sit</text>
  <text x="145" y="90" text-anchor="end" style="font:300 12px 'Montserrat',sans-serif;fill:#fff">Amet</text>
  <text class="body" x="145" y="100" text-anchor="end" style="fill:#fff">Lorem ipsum dolor sit amet, consetetur</text>
  <text class="body" x="145" y="104" text-anchor="end" style="fill:#fff">sadipscing elitr, sed diam nonumy eirmod</text>
  <circle role="img" aria-label="Photo of a stethoscope in hand" cx="225" cy="85" r="52" fill="url(#photo)" stroke="#fff" stroke-width="2"/>
  <circle class="ring" cx="225" cy="85" r="58" pathLength="100" stroke-dasharray="40 60" transform="rotate(95 225 85)"/>
  <circle cx="16" cy="152" r="5" fill="none" stroke="#fff" stroke-width="1"/>
  <text class="brand" x="25" y="154" style="fill:#fff;font-size:5.5px">REGIONAL HARMONY INSTITUTE</text>
</svg>
</div>
<div class="slide col-r" style="top:166px">
<svg viewBox="0 0 300 170">
  <text class="title" x="16" y="20">LOREM IPSUM</text>
  <circle class="node" cx="281" cy="18" r="6"/>
  <circle role="img" aria-label="Photo of a doctor writing notes" cx="75" cy="92" r="52" fill="url(#photo)"/>
  <circle class="ring" cx="75" cy="92" r="58" pathLength="100" stroke-dasharray="40 60" transform="rotate(95 75 92)"/>
  <text class="lead" x="145" y="40">Lorem ipsum dolor sit amet, consetetur sadipscing elitr,</text>
  <text class="lead" x="145" y="45">sed diam nonumy eirmod tempor invidunt ut labore.</text>
  <g class="body">
    <text x="145" y="56">At vero eos et accusam et justo duo dolores et ea rebum clita.</text>
    <text x="145" y="61">Stet clita kasd gubergren, no sea takimata sanctus est lorem.</text>
    <text x="145" y="66">Ipsum dolor sit amet, consetetur sadipscing elitr sed diam.</text>
    <text x="145" y="71">Nonumy eirmod tempor invidunt ut labore et dolore magna.</text>
    <text x="145" y="82">Aliquyam erat, sed diam voluptua at vero eos et accusam.</text>
    <text x="145" y="87">Justo duo dolores et ea rebum, stet clita kasd gubergren.</text>
    <text x="145" y="92">No sea takimata sanctus est lorem ipsum dolor sit amet.</text>
    <text x="145" y="97">Consetetur sadipscing elitr, sed diam nonumy eirmod tempor.</text>
  </g>
  <circle class="line" cx="20" cy="162" r="3"/>
  <text class="foot" x="284" y="163" text-anchor="end">REGIONAL HARMONY INSTITUTE</text>
</svg>
</div>

<!-- Row 3 -->
<div class="slide col-l" style="top:310px">
<svg viewBox="0 0 300 170">
  <text class="title" x="16" y="20">LOREM IPSUM</text>
  <circle class="node" cx="281" cy="18" r="6"/>
  <g class="body">
    <text x="16" y="29">Lorem ipsum dolor sit amet, consetetur sadipscing elitr, sed diam nonumy</text>
    <text x="16" y="33">eirmod tempor invidunt ut labore et dolore magna aliquyam erat, sed diam</text>
  </g>
  <circle class="navyfill" cx="26" cy="63" r="1.3"/><text class="label" x="31" y="64">Lorem Ipsum Dolor Sit Amet</text>
  <text class="body" x="31" y="70">Lorem ipsum dolor sit amet, consetetur sadipscing elitr.</text>
  <circle class="navyfill" cx="26" cy="94" r="1.3"/><text class="label" x="31" y="95">Lorem Ipsum Dolor Sit Amet</text>
  <text class="body" x="31" y="101">Lorem ipsum dolor sit amet, consetetur sadipscing elitr.</text>
  <circle class="navyfill" cx="26" cy="125" r="1.3"/><text class="label" x="31" y="126">Lorem Ipsum Dolor Sit Amet</text>
  <text class="body" x="31" y="132">Lorem ipsum dolor sit amet, consetetur sadipscing elitr.</text>
  <circle role="img" aria-label="Photo of two doctors looking at a tablet" cx="232" cy="88" r="50" fill="url(#photo)"/>
  <circle class="ring" cx="232" cy="88" r="56" pathLength="100" stroke-dasharray="40 60" transform="rotate(-85 232 88)"/>
  <circle class="line" cx="20" cy="162" r="3"/>
  <text class="foot" x="284" y="163" text-anchor="end">REGIONAL HARMONY INSTITUTE</text>
</svg>
</div>
<div class="slide col-r" style="top:310px">
<svg viewBox="0 0 300 170">
  <text class="title" x="16" y="20">LOREM IPSUM</text>
  <circle class="node" cx="281" cy="18" r="6"/>
  <circle role="img" aria-label="Photo of a smiling nurse in scrubs" cx="68" cy="90" r="52" fill="url(#photo)"/>
  <circle class="ring" cx="68" cy="90" r="58" pathLength="100" stroke-dasharray="40 60" transform="rotate(-85 68 90)"/>
  <text class="lead" x="145" y="52">Lorem ipsum dolor sit amet, consetetur sadipscing elitr,</text>
  <text class="lead" x="145" y="57">sed diam nonumy eirmod tempor invidunt ut labore et</text>
  <text class="lead" x="145" y="62">dolore magna aliquyam erat, sed diam voluptua.</text>
  <g fill="none" stroke="var(--navy)" stroke-width=".8">
    <circle cx="152" cy="90" r="3"/><circle cx="230" cy="90" r="3"/>
    <circle cx="152" cy="120" r="3"/><rect x="227" y="117" width="6" height="6"/>
  </g>
  <g class="body">
    <text x="160" y="84" class="label" style="font-size:2.8px">Lorem Ipsum</text><text x="160" y="89">Lorem ipsum dolor sit amet</text><text x="160" y="93">consetetur sadipscing elitr.</text>
    <text x="238" y="84" class="label" style="font-size:2.8px">Lorem Ipsum</text><text x="238" y="89">Lorem ipsum dolor sit amet</text><text x="238" y="93">consetetur sadipscing elitr.</text>
    <text x="160" y="114" class="label" style="font-size:2.8px">Lorem Ipsum</text><text x="160" y="119">Lorem ipsum dolor sit amet</text><text x="160" y="123">consetetur sadipscing elitr.</text>
    <text x="238" y="114" class="label" style="font-size:2.8px">Lorem Ipsum</text><text x="238" y="119">Lorem ipsum dolor sit amet</text><text x="238" y="123">consetetur sadipscing elitr.</text>
  </g>
  <circle class="line" cx="20" cy="162" r="3"/>
  <text class="foot" x="284" y="163" text-anchor="end">REGIONAL HARMONY INSTITUTE</text>
</svg>
</div>

<!-- Row 4 -->
<div class="slide col-l" style="top:455px">
<svg viewBox="0 0 300 170">
  <text class="title" x="16" y="20">LOREM IPSUM</text>
  <circle class="node" cx="281" cy="18" r="6"/>
  <g class="body">
    <text x="16" y="29">Lorem ipsum dolor sit amet, consetetur sadipscing elitr, sed diam nonumy eirmod tempor invidunt ut labore et dolore magna.</text>
    <text x="16" y="33">At vero eos et accusam et justo duo dolores et ea rebum. Stet clita kasd gubergren, no sea takimata sanctus est.</text>
  </g>
  <line class="line" x1="60" y1="88" x2="240" y2="88"/>
  <g fill="none" stroke="var(--navy)" stroke-width=".8">
    <rect x="56" y="72" width="8" height="10"/><path d="M150 72 v10 M145 75 h10 M147 79 h6"/><path d="M236 82 h8 l-2 -6 h-4 z M240 76 v-4"/>
  </g>
  <g class="navyfill"><circle cx="60" cy="88" r="1.4"/><circle cx="150" cy="88" r="1.4"/><circle cx="240" cy="88" r="1.4"/></g>
  <g text-anchor="middle">
    <text class="label" x="60" y="97">Lorem ipsum</text><text class="label" x="60" y="101">dolor sit amet</text>
    <text class="body" x="60" y="108">Lorem ipsum dolor sit amet,</text><text class="body" x="60" y="112">consetetur sadipscing elitr.</text>
    <text class="label" x="150" y="97">Lorem ipsum</text><text class="label" x="150" y="101">dolor sit amet</text>
    <text class="body" x="150" y="108">Lorem ipsum dolor sit amet,</text><text class="body" x="150" y="112">consetetur sadipscing elitr.</text>
    <text class="label" x="240" y="97">Lorem ipsum</text><text class="label" x="240" y="101">dolor sit amet</text>
    <text class="body" x="240" y="108">Lorem ipsum dolor sit amet,</text><text class="body" x="240" y="112">consetetur sadipscing elitr.</text>
  </g>
  <circle class="line" cx="20" cy="162" r="3"/>
  <text class="foot" x="284" y="163" text-anchor="end">REGIONAL HARMONY INSTITUTE</text>
</svg>
</div>
<div class="slide col-r" style="top:455px">
<svg viewBox="0 0 300 170">
  <text class="title" x="16" y="20">LOREM IPSUM</text>
  <circle class="node" cx="281" cy="18" r="6"/>
  <g class="navyfill">
    <circle cx="22" cy="50" r="2.5"/><circle cx="22" cy="77" r="2.5"/><circle cx="22" cy="104" r="2.5"/><circle cx="22" cy="131" r="2.5"/>
    <circle cx="95" cy="50" r="2.5"/><circle cx="95" cy="77" r="2.5"/><circle cx="95" cy="104" r="2.5"/><circle cx="95" cy="131" r="2.5"/>
  </g>
  <g class="body">
    <text x="30" y="46" class="label" style="font-size:2.6px">Lorem Ipsum</text><text x="30" y="51">Lorem ipsum dolor sit</text><text x="30" y="55">amet consetetur elitr.</text>
    <text x="30" y="73" class="label" style="font-size:2.6px">Lorem Ipsum</text><text x="30" y="78">Lorem ipsum dolor sit</text><text x="30" y="82">amet consetetur elitr.</text>
    <text x="30" y="100" class="label" style="font-size:2.6px">Lorem Ipsum</text><text x="30" y="105">Lorem ipsum dolor sit</text><text x="30" y="109">amet consetetur elitr.</text>
    <text x="30" y="127" class="label" style="font-size:2.6px">Lorem Ipsum</text><text x="30" y="132">Lorem ipsum dolor sit</text><text x="30" y="136">amet consetetur elitr.</text>
    <text x="103" y="46" class="label" style="font-size:2.6px">Lorem Ipsum</text><text x="103" y="51">Lorem ipsum dolor sit</text><text x="103" y="55">amet consetetur elitr.</text>
    <text x="103" y="73" class="label" style="font-size:2.6px">Lorem Ipsum</text><text x="103" y="78">Lorem ipsum dolor sit</text><text x="103" y="82">amet consetetur elitr.</text>
    <text x="103" y="100" class="label" style="font-size:2.6px">Lorem Ipsum</text><text x="103" y="105">Lorem ipsum dolor sit</text><text x="103" y="109">amet consetetur elitr.</text>
    <text x="103" y="127" class="label" style="font-size:2.6px">Lorem Ipsum</text><text x="103" y="132">Lorem ipsum dolor sit</text><text x="103" y="136">amet consetetur elitr.</text>
  </g>
  <circle role="img" aria-label="Photo of a nurse holding a phone" cx="240" cy="100" r="52" fill="url(#photo)"/>
  <circle class="ring" cx="240" cy="100" r="58" pathLength="100" stroke-dasharray="40 60" transform="rotate(95 240 100)"/>
  <circle class="line" cx="20" cy="162" r="3"/>
  <text class="foot" x="284" y="163" text-anchor="end">REGIONAL HARMONY INSTITUTE</text>
</svg>
</div>

<!-- Row 5 -->
<div class="slide col-l" style="top:600px">
<svg viewBox="0 0 300 170">
  <circle class="node" cx="281" cy="18" r="6"/>
  <g class="line" style="stroke:var(--ink);stroke-width:.5">
    <path d="M100 75 H70 M100 75 L65 55 M100 75 L60 95 M135 75 H165 M135 75 L170 55 M135 75 L170 95"/>
    <path d="M105 88 L70 128 M110 88 L90 128 M115 88 L110 128 M120 88 L130 128 M125 88 L150 128 M130 88 L170 128"/>
  </g>
  <path class="navyfill" d="M95 88 a12 12 0 0 1 4 -22 a14 14 0 0 1 26 -4 a11 11 0 0 1 13 12 a8 8 0 0 1 -3 14 z"/>
  <circle cx="117" cy="76" r="7" fill="none" stroke="#fff" stroke-width="1.4"/>
  <g class="node">
    <circle cx="65" cy="55" r="4.5"/><circle cx="60" cy="75" r="4.5"/><circle cx="60" cy="95" r="4.5"/>
    <circle cx="170" cy="55" r="4.5"/><circle cx="170" cy="75" r="4.5"/><circle cx="170" cy="95" r="4.5"/>
    <circle cx="70" cy="130" r="4.5"/><circle cx="90" cy="130" r="4.5"/><circle cx="110" cy="130" r="4.5"/>
    <circle cx="130" cy="130" r="4.5"/><circle cx="150" cy="130" r="4.5"/><circle cx="170" cy="130" r="4.5"/>
  </g>
  <text class="title" x="210" y="65">LOREM IPSUM</text>
  <g class="body">
    <text x="198" y="74">Lorem ipsum dolor sit amet, consetetur</text>
    <text x="198" y="78">sadipscing elitr, sed diam nonumy eirmod</text>
    <text x="198" y="82">tempor invidunt ut labore et dolore magna</text>
    <text x="198" y="86">aliquyam erat, sed diam voluptua at vero</text>
    <text x="198" y="90">eos et accusam et justo duo dolores et ea</text>
    <text x="198" y="94">rebum stet clita kasd gubergren no sea.</text>
  </g>
  <circle class="line" cx="20" cy="162" r="3"/>
  <text class="foot" x="284" y="163" text-anchor="end">REGIONAL HARMONY INSTITUTE</text>
</svg>
</div>
<div class="slide col-r" style="top:600px">
<svg viewBox="0 0 300 170">
  <circle class="node" cx="281" cy="18" r="6"/>
  <text class="title" x="65" y="80">LOREM IPSUM</text>
  <g class="body">
    <text x="45" y="89">Lorem ipsum dolor sit amet, consetetur</text>
    <text x="45" y="93">sadipscing elitr, sed diam nonumy eirmod</text>
    <text x="45" y="97">tempor invidunt ut labore et dolore magna</text>
    <text x="45" y="101">aliquyam erat, sed diam voluptua at vero</text>
    <text x="45" y="105">eos et accusam et justo duo dolores et ea</text>
    <text x="45" y="109">rebum stet clita kasd gubergren no sea.</text>
  </g>
  <g class="line" style="stroke:var(--ink);stroke-width:.4;stroke-dasharray:1 1">
    <path d="M245 30 L198 50 L190 73 L245 30 L225 75 L190 73 L210 108 L225 75 L268 95 L245 30 L280 55 L268 95 L250 125 L225 75 M210 108 L250 125 L212 140 L210 108 M198 50 L225 75 M280 55 L225 75"/>
  </g>
  <g class="node">
    <circle cx="245" cy="30" r="6"/><circle cx="198" cy="50" r="5"/><circle cx="190" cy="73" r="5"/>
    <circle cx="225" cy="75" r="7"/><circle cx="280" cy="55" r="4"/><circle cx="268" cy="95" r="6"/>
    <circle cx="210" cy="108" r="6"/><circle cx="250" cy="125" r="5"/><circle cx="212" cy="140" r="4"/>
  </g>
  <circle class="line" cx="20" cy="162" r="3"/>
  <text class="foot" x="284" y="163" text-anchor="end">REGIONAL HARMONY INSTITUTE</text>
</svg>
</div>

<!-- Row 6 -->
<div class="slide col-l" style="top:745px">
<svg viewBox="0 0 300 170">
  <text class="title" x="16" y="20">LOREM IPSUM</text>
  <circle class="node" cx="281" cy="18" r="6"/>
  <g class="body">
    <text x="16" y="30">Lorem ipsum dolor sit amet</text><text x="16" y="34">consetetur sadipscing elitr, sed</text>
    <text x="16" y="38">diam nonumy eirmod tempor</text><text x="16" y="42">invidunt ut labore et dolore</text>
    <text x="16" y="46">magna aliquyam erat, sed diam</text><text x="16" y="50">voluptua at vero eos et accusam</text>
    <text x="16" y="54">et justo duo dolores et ea rebum.</text>
  </g>
  <path class="line" style="stroke:var(--ink);stroke-width:.5" d="M180 60 V75 M95 75 H265 M95 75 V92 M180 75 V92 M265 75 V92"/>
  <circle class="navyfill" cx="180" cy="45" r="14"/>
  <circle cx="180" cy="45" r="17" fill="none" stroke="var(--navy)" stroke-width="1" pathLength="100" stroke-dasharray="50 50" transform="rotate(180 180 45)"/>
  <g class="node"><circle cx="95" cy="100" r="8"/><circle cx="180" cy="100" r="8"/><circle cx="265" cy="100" r="8"/></g>
  <g text-anchor="middle">
    <text class="label" x="95" y="116">Lorem ipsum</text><text class="label" x="95" y="120">dolor sit amet</text>
    <text class="body" x="95" y="127">Lorem ipsum dolor sit amet,</text><text class="body" x="95" y="131">consetetur sadipscing elitr.</text>
    <text class="label" x="180" y="116">Lorem ipsum</text><text class="label" x="180" y="120">dolor sit amet</text>
    <text class="body" x="180" y="127">Lorem ipsum dolor sit amet,</text><text class="body" x="180" y="131">consetetur sadipscing elitr.</text>
    <text class="label" x="265" y="116">Lorem ipsum</text><text class="label" x="265" y="120">dolor sit amet</text>
    <text class="body" x="265" y="127">Lorem ipsum dolor sit amet,</text><text class="body" x="265" y="131">consetetur sadipscing elitr.</text>
  </g>
  <circle class="line" cx="20" cy="162" r="3"/>
  <text class="foot" x="284" y="163" text-anchor="end">REGIONAL HARMONY INSTITUTE</text>
</svg>
</div>
<div class="slide col-r" style="top:745px">
<svg viewBox="0 0 300 170">
  <text class="title" x="16" y="20">LOREM IPSUM</text>
  <circle class="node" cx="281" cy="18" r="6"/>
  <g class="body">
    <text x="16" y="30">Lorem ipsum dolor sit amet</text><text x="16" y="34">consetetur sadipscing elitr, sed</text>
    <text x="16" y="38">diam nonumy eirmod tempor</text><text x="16" y="42">invidunt ut labore et dolore</text>
    <text x="16" y="46">magna aliquyam erat, sed diam</text><text x="16" y="50">voluptua at vero eos et accusam.</text>
  </g>
  <path class="line" style="stroke:var(--ink);stroke-width:.5" d="M180 60 V72 M95 72 H265 M95 72 V85 M180 72 V85 M265 72 V85 M95 103 V110 M72 110 H118 M72 110 V118 M118 110 V118 M180 103 V110 M157 110 H203 M157 110 V118 M203 110 V118 M265 103 V110 M242 110 H288 M242 110 V118 M288 110 V118"/>
  <circle class="navyfill" cx="180" cy="42" r="14"/>
  <circle cx="180" cy="42" r="17" fill="none" stroke="var(--navy)" stroke-width="1" pathLength="100" stroke-dasharray="50 50" transform="rotate(180 180 42)"/>
  <g class="node">
    <circle cx="95" cy="94" r="8"/><circle cx="180" cy="94" r="8"/><circle cx="265" cy="94" r="8"/>
    <circle cx="72" cy="126" r="7"/><circle cx="118" cy="126" r="7"/><circle cx="157" cy="126" r="7"/>
    <circle cx="203" cy="126" r="7"/><circle cx="242" cy="126" r="7"/><circle cx="288" cy="126" r="7"/>
  </g>
  <circle class="line" cx="20" cy="162" r="3"/>
  <text class="foot" x="284" y="163" text-anchor="end">REGIONAL HARMONY INSTITUTE</text>
</svg>
</div>

<!-- Row 7 -->
<div class="slide col-l" style="top:890px">
<svg viewBox="0 0 300 170">
  <text class="title" x="16" y="20">LOREM IPSUM</text>
  <circle class="node" cx="281" cy="18" r="6"/>
  <g fill="none" stroke="#7a7f88" stroke-width=".8">
    <path d="M55 66 Q72 56 88 66"/><path d="M110 104 Q127 114 143 104"/>
    <path d="M165 66 Q182 56 198 66"/><path d="M220 104 Q237 114 253 104"/>
  </g>
  <g class="node" style="stroke-width:2">
    <circle cx="45" cy="85" r="20"/><circle cx="100" cy="85" r="20"/><circle cx="155" cy="85" r="20"/><circle cx="210" cy="85" r="20"/>
  </g>
  <circle cx="265" cy="85" r="20" fill="#4a4d52" stroke="var(--navy)" stroke-width="2"/>
  <g text-anchor="middle" class="label" style="font-size:2.6px">
    <text x="45" y="92">Lorem ipsum</text><text x="100" y="92">Lorem ipsum</text><text x="155" y="92">Lorem ipsum</text><text x="210" y="92">Lorem ipsum</text>
    <text x="265" y="92" style="fill:#fff">Lorem</text>
  </g>
  <g text-anchor="middle" class="body">
    <text x="45" y="115">Lorem ipsum dolor sit</text><text x="45" y="119">amet consetetur elitr.</text>
    <text x="100" y="120">Lorem ipsum dolor sit</text><text x="100" y="124">amet consetetur elitr.</text>
    <text x="155" y="115">Lorem ipsum dolor sit</text><text x="155" y="119">amet consetetur elitr.</text>
    <text x="210" y="120">Lorem ipsum dolor sit</text><text x="210" y="124">amet consetetur elitr.</text>
  </g>
  <circle class="line" cx="20" cy="162" r="3"/>
  <text class="foot" x="284" y="163" text-anchor="end">REGIONAL HARMONY INSTITUTE</text>
</svg>
</div>
<div class="slide col-r" style="top:890px">
<svg viewBox="0 0 300 170">
  <circle class="node" cx="281" cy="18" r="6"/>
  <rect x="18" y="8" width="98" height="142" rx="3" fill="#fff" stroke="var(--navy)" stroke-width="1"/>
  <rect role="img" aria-label="Portrait photo of a consultant in a suit" x="22" y="12" width="90" height="62" fill="url(#photo)"/>
  <g class="label" style="font-size:3px">
    <text x="24" y="90">Age:</text><text x="48" y="90">45</text>
    <text x="24" y="96">Work:</text><text x="48" y="96">Consultant</text>
    <text x="24" y="102">Family:</text><text x="48" y="102">Married with kids</text>
    <text x="24" y="108">Location:</text><text x="48" y="108">Maple Bay</text>
  </g>
  <rect x="14" y="118" width="100" height="20" rx="3" fill="#4a4d52"/>
  <g class="body" text-anchor="middle" style="fill:#fff">
    <text x="64" y="125">Lorem ipsum dolor sit amet, consetetur</text>
    <text x="64" y="129">sadipscing elitr, sed diam nonumy eirmod</text>
    <text x="64" y="133">tempor invidunt ut labore et dolore.</text>
  </g>
  <text x="125" y="28" style="font:400 13px 'Montserrat',sans-serif;fill:var(--navy)">Name</text>
  <g class="body">
    <text x="125" y="37">Lorem ipsum dolor sit amet, consetetur sadipscing</text>
    <text x="125" y="41">elitr, sed diam nonumy eirmod tempor invidunt ut</text>
    <text x="125" y="45">labore et dolore magna aliquyam erat, sed diam.</text>
    <text x="125" y="55">At vero eos et accusam et justo duo dolores et ea</text>
    <text x="125" y="59">rebum. Stet clita kasd gubergren, no sea takimata.</text>
    <text x="125" y="69">Sanctus est lorem ipsum dolor sit amet, consetetur</text>
    <text x="125" y="73">sadipscing elitr, sed diam nonumy eirmod tempor.</text>
    <text x="125" y="83">Invidunt ut labore et dolore magna aliquyam erat.</text>
    <text x="125" y="87">Sed diam voluptua at vero eos et accusam et justo.</text>
  </g>
  <text class="label" x="240" y="41" style="font-size:2.8px">SKILLS</text>
  <g>
    <rect x="240" y="48" width="50" height="2" rx="1" fill="var(--rule)"/><rect x="240" y="48" width="40" height="2" rx="1" class="navyfill"/>
    <rect x="240" y="58" width="50" height="2" rx="1" fill="var(--rule)"/><rect x="240" y="58" width="30" height="2" rx="1" class="navyfill"/>
    <rect x="240" y="68" width="50" height="2" rx="1" fill="var(--rule)"/><rect x="240" y="68" width="35" height="2" rx="1" class="navyfill"/>
    <rect x="240" y="100" width="50" height="2" rx="1" fill="var(--rule)"/><rect x="240" y="100" width="25" height="2" rx="1" class="navyfill"/>
    <rect x="240" y="110" width="50" height="2" rx="1" fill="var(--rule)"/><rect x="240" y="110" width="42" height="2" rx="1" class="navyfill"/>
    <rect x="240" y="120" width="50" height="2" rx="1" fill="var(--rule)"/><rect x="240" y="120" width="32" height="2" rx="1" class="navyfill"/>
  </g>
  <circle class="line" cx="20" cy="162" r="3"/>
  <text class="foot" x="284" y="163" text-anchor="end">REGIONAL HARMONY INSTITUTE</text>
</svg>
</div>

<!-- Row 8 -->
<div class="slide col-l" style="top:1034px">
<svg viewBox="0 0 300 170">
  <circle role="img" aria-label="Photo of hands typing on a laptop" cx="60" cy="85" r="42" fill="url(#photo)"/>
  <circle class="ring" cx="60" cy="85" r="47" style="stroke-width:4" pathLength="100" stroke-dasharray="40 60" transform="rotate(-85 60 85)"/>
  <circle class="node" cx="152" cy="52" r="8"/>
  <text class="brand" x="164" y="50" style="font-size:9px">REGIONAL HARMONY</text>
  <text class="brand" x="164" y="58" style="font-size:6px">INSTITUTE</text>
  <g class="node" style="stroke-width:.8"><circle cx="158" cy="97" r="5"/><circle cx="158" cy="113" r="5"/><circle cx="158" cy="129" r="5"/></g>
  <line class="line" x1="178" y1="92" x2="178" y2="140"/>
  <g text-anchor="end">
    <text class="lead" x="270" y="103" style="font-size:2.6px">CONNECTING THE BRIGHTEST</text>
    <text class="lead" x="270" y="107" style="font-size:2.6px">MINDS IN HEALTHCARE</text>
    <text class="body" x="270" y="115">Lorem ipsum dolor</text>
    <text class="body" x="270" y="119">+123 456 7890</text>
    <text class="body" x="270" y="123">contact@regionalharmonyinstitute.com</text>
    <text class="body" x="270" y="127">www.regionalharmonyinstitute.com</text>
    <text class="body" x="270" y="131">Lorem ipsum dolor sit</text>
  </g>
</svg>
</div>
<div class="slide col-r" style="top:1034px">
<svg viewBox="0 0 300 170">
  <circle cx="35" cy="42" r="13" fill="none" stroke="var(--navy)" stroke-width="2"/>
  <text class="brand" x="55" y="42" style="font-size:13px">REGIONAL HARMONY</text>
  <text class="brand" x="55" y="52" style="font-size:8px">INSTITUTE</text>
  <g class="node" style="stroke-width:.8"><circle cx="140" cy="140" r="5"/><circle cx="155" cy="140" r="5"/><circle cx="170" cy="140" r="5"/></g>
  <line class="line" x1="195" y1="115" x2="195" y2="160"/>
  <g>
    <text class="label" x="202" y="120" style="font-size:2.8px">Lorem ipsum dolor</text>
    <text class="body" x="202" y="126">+123 456 7890</text>
    <text class="body" x="202" y="130">contact@regionalharmonyinstitute.com</text>
    <text class="body" x="202" y="134">www.regionalharmonyinstitute.com</text>
    <text class="body" x="202" y="138">Lorem ipsum dolor</text>
    <text class="body" x="202" y="142">Sit amet consetetur</text>
  </g>
</svg>
</div>
</div>
</body>
</html>
```